A clean crisp business card for a Landscape Construction company. Designed to be easy to read contact/ info and also be appealing/interesting, unlike a traditional business card.

Industry/Entity Type

Landscape Construction

Contact Information for Business Card

Company name : Bramblecrest Landscape Construction, phone number: (877) 62Vales, website:Bramblecrestlandscapes.example, Email, sales@bramblecrestlandscapes.example

Requirements
Nice to have
• Luxurious finishes/ details…. Icons or emblems next to contact info
Should not have
• Clipart or general pictures

```html
<!DOCTYPE html>
<html lang="en">
<head>
<meta charset="utf-8">
<title>Bramblecrest Landscape Construction – Business Card</title>
<link rel="stylesheet" href="https://fonts.googleapis.com/css2?family=Cinzel:wght@600;700&family=Arimo:wght@400&display=swap">
<style>
  :root {
    --page-bg: #e9e9e7;
    --card-bg: #242424;
    --card-bg-deep: #1c1c1c;
    --brand-blue: #1f6fc4;
    --brand-green: #9ccd2e;
    --text-light: #f2f2f2;
    --pattern-light: #5a5a5a;
    --pattern-dark: #1e1e1e;
  }
  * { box-sizing: border-box; margin: 0; padding: 0; }
  html, body { width: 1200px; height: 900px; overflow: hidden; }
  body {
    background: var(--page-bg);
    display: flex;
    flex-direction: column;
    align-items: center;
    justify-content: center;
    gap: 36px;
  }
  .card {
    position: relative;
    width: 700px;
    height: 400px;
    background: var(--card-bg);
    overflow: hidden;
    box-shadow: 0 10px 28px rgba(0,0,0,0.25);
  }

  /* ---------- Front ---------- */
  .brand {
    position: absolute;
    left: 58px;
    top: 142px;
    width: 250px;
    color: var(--brand-blue);
    font-family: "Cinzel", serif;
    font-weight: 700;
    text-align: center;
  }
  .brand-dot {
    display: block;
    width: 34px;
    height: 34px;
    border-radius: 50%;
    background: var(--brand-blue);
    margin: 0 auto 12px;
  }
  .brand-name { font-size: 30px; letter-spacing: 1px; line-height: 1; }
  .brand-sub { font-size: 10.5px; letter-spacing: 3.2px; margin-top: 8px; }

  .divider {
    position: absolute;
    left: 338px;
    top: 118px;
    width: 1px;
    height: 150px;
    background: linear-gradient(var(--brand-green), var(--brand-blue));
  }

  .person {
    position: absolute;
    left: 372px;
    top: 128px;
  }
  .person-name {
    font-family: "Cinzel", serif;
    font-weight: 700;
    font-size: 27px;
    letter-spacing: 1px;
    line-height: 1;
  }
  .person-name .first { color: var(--brand-blue); }
  .person-name .last { color: var(--brand-green); }
  .person-role {
    font-family: "Arimo", sans-serif;
    color: var(--text-light);
    font-size: 17px;
    margin-top: 5px;
  }

  .contacts {
    list-style: none;
    margin-top: 18px;
    font-family: "Arimo", sans-serif;
    color: var(--text-light);
    font-size: 15.5px;
  }
  .contacts li {
    display: flex;
    align-items: center;
    gap: 9px;
    margin-bottom: 7px;
  }
  .contacts svg { width: 14px; height: 14px; flex: none; }

  .accent-band {
    position: absolute;
    left: 0;
    right: 0;
    bottom: 36px;
    height: 10px;
    background: var(--brand-green);
  }

  /* ---------- Back ---------- */
  .card-back { background: var(--card-bg-deep); }
  .emblem-pattern {
    position: absolute;
    inset: 0;
    background: linear-gradient(135deg, var(--pattern-dark) 0%, #2a2a2a 45%, var(--pattern-light) 100%);
  }
  .back-brand {
    position: absolute;
    left: 40px;
    bottom: 34px;
    display: flex;
    align-items: center;
    gap: 8px;
    font-family: "Cinzel", serif;
    font-weight: 700;
    font-size: 14px;
    letter-spacing: 1px;
    color: var(--brand-blue);
  }
  .back-brand .brand-dot { width: 16px; height: 16px; margin: 0; }
</style>
</head>
<body>

  <section class="card card-front" aria-label="Business card front">
    <div class="brand">
      <span class="brand-dot"></span>
      <div class="brand-name">Bramblecrest</div>
      <div class="brand-sub">Landscape Construction</div>
    </div>

    <div class="divider"></div>

    <div class="person">
      <h1 class="person-name"><span class="first">Dylan</span> <span class="last">Marsh</span></h1>
      <p class="person-role">Founder</p>
      <ul class="contacts">
        <li>
          <svg viewBox="0 0 16 16" aria-hidden="true"><path fill="#9ccd2e" d="M3.6 1.5l2.3 2.3-1.4 2a9 9 0 0 0 5.7 5.7l2-1.4 2.3 2.3-1.6 2C7.5 14.3 1.7 8.5 1.6 3.1z"/></svg>
          <span>(877) 62Vales</span>
        </li>
        <li>
          <svg viewBox="0 0 16 16" aria-hidden="true"><rect x="1" y="3" width="14" height="10" rx="1" fill="#9ccd2e"/><path d="M1.5 3.6L8 9l6.5-5.4" fill="none" stroke="#242424" stroke-width="1.3"/></svg>
          <span>sales@bramblecrestlandscapes.example</span>
        </li>
        <li>
          <svg viewBox="0 0 16 16" aria-hidden="true"><circle cx="8" cy="8" r="6.5" fill="none" stroke="#9ccd2e" stroke-width="1.5"/><ellipse cx="8" cy="8" rx="2.8" ry="6.5" fill="none" stroke="#9ccd2e" stroke-width="1.2"/><path d="M1.5 8h13" stroke="#9ccd2e" stroke-width="1.2"/></svg>
          <span>bramblecrestlandscapes.example</span>
        </li>
      </ul>
    </div>

    <div class="accent-band"></div>
  </section>

  <section class="card card-back" aria-label="Business card back">
    <div class="emblem-pattern" role="img" aria-label="Repeating embossed brand emblem pattern in dark and silver grey tones"></div>
    <div class="back-brand"><span class="brand-dot"></span>Bramblecrest</div>
  </section>

</body>
</html>
```